Flyer Design for Halvern Works

Contracting Services
Domestic | Rural | Commercial | Industrial markets.
Electrical, Refrigeration, Air-conditioning, Solar, Data, Communications, TV, Satellite, Wireless

```html
<!DOCTYPE html>
<html lang="en">
<head>
<meta charset="utf-8">
<title>Halvern Works – Contracting Services Flyer</title>
<link rel="stylesheet" href="https://fonts.googleapis.com/css2?family=Roboto+Condensed:wght@400;700&family=Roboto:wght@400&display=swap">
<style>
  :root{
    --page:#e9eef1;
    --flyer:#5ec7e4;
    --flyer-light:#8ad8ee;
    --stripe:#2aa6cf;
    --ink:#15222e;
    --rule:#2c6f97;
    --band:#a8e3f3;
    --licence:#6fb8cf;
    --licence-mid:#9fdcef;
    --ring:#ffffff;
  }
  *{box-sizing:border-box;margin:0;padding:0}
  html,body{width:1200px;height:1041px;overflow:hidden;background:var(--page)}
  .flyer{
    position:absolute;left:252px;top:30px;width:696px;height:980px;overflow:hidden;
    background:radial-gradient(ellipse at 45% 45%, var(--flyer-light) 0%, var(--flyer) 60%);
    font-family:"Roboto Condensed",Arial,sans-serif;color:var(--ink);
    box-shadow:0 4px 18px rgba(0,0,0,.18);
  }
  .top-stripe{position:absolute;left:0;top:0;width:100%;height:9px;background:var(--stripe)}
  .brand{position:absolute;left:0;top:44px;width:100%;display:flex;justify-content:center;align-items:center;gap:12px}
  .brand-dot{width:40px;height:40px;border-radius:50%;background:var(--ink)}
  .brand-name{font-weight:700;font-size:40px;letter-spacing:1px;color:var(--ink);text-transform:uppercase}
  .service{position:absolute;left:55px}
  .service h2{font-size:13.5px;font-weight:700;letter-spacing:.3px;padding-bottom:4px;border-bottom:1.5px solid var(--rule)}
  .service p{font-family:"Roboto",Arial,sans-serif;font-size:12.3px;line-height:16.6px;margin-top:8px}
  .photo{position:absolute;border-radius:50%;border:3px solid var(--ring)}
  .photo-solar{left:570px;top:119px;width:110px;height:110px;background:linear-gradient(160deg,#c7a98a,#2c4f9c 60%,#1d3a7c)}
  .photo-fridge{left:435px;top:219px;width:122px;height:122px;background:linear-gradient(90deg,#5b6d73,#8fa3a6 50%,#6c8a5a)}
  .photo-wind{left:522px;top:294px;width:232px;height:232px;background:linear-gradient(180deg,#5b8fc2 0%,#e3b283 40%,#2d4f9a 55%,#1b3b86 100%)}
  .photo-server{left:580px;top:545px;width:116px;height:116px;background:linear-gradient(120deg,#c9c2b6,#7d8a90 55%,#3a4c5a)}
  .photo-worker{position:absolute;left:558px;top:696px;width:124px;height:209px;background:linear-gradient(180deg,#d9b49a 0%,#3a5f96 35%,#2a4a7a 70%,#7a5a3c 100%)}
  .terms{position:absolute;left:54px;top:880px;font-family:"Roboto",Arial,sans-serif;font-size:10px}
  .contact-band{position:absolute;left:0;top:907px;width:100%;height:37px;background:var(--band);display:flex;align-items:center;font-size:13px;font-weight:700}
  .contact{position:absolute;display:flex;align-items:center;gap:7px}
  .contact svg{width:12px;height:12px;fill:var(--ink)}
  .licences{position:absolute;left:0;top:950px;width:100%;height:30px;display:flex;font-size:12px;font-weight:700}
  .licences div{flex:1;display:flex;align-items:center;justify-content:center;background:var(--licence)}
  .licences div.mid{background:var(--licence-mid)}
</style>
</head>
<body>
<div class="flyer">
  <div class="top-stripe"></div>

  <div class="brand">
    <span class="brand-dot"></span>
    <span class="brand-name">Halvern Works</span>
  </div>

  <div class="photo photo-solar" role="img" aria-label="Photo of technicians installing solar panels on a roof"></div>
  <div class="photo photo-fridge" role="img" aria-label="Photo of an outdoor air conditioning unit"></div>
  <div class="photo photo-wind" role="img" aria-label="Photo of wind turbines at sunset above a solar panel array"></div>
  <div class="photo photo-server" role="img" aria-label="Photo of a technician working at a server rack"></div>
  <div class="photo-worker" role="img" aria-label="Photo of a tradesman in safety glasses wearing a tool belt"></div>

  <section class="service" style="top:157px;width:373px">
    <h2>ELECTRICAL</h2>
    <p>Service Repair Install all electrical issues from powerpoints, to swicthboards, to installing power poles. Also extensive knowledge on motors, pumps and water irrigation systems. PLC's and turn key automation systems.</p>
  </section>

  <section class="service" style="top:289px;width:373px">
    <h2>REFRIGERATION</h2>
    <p>Service Repair Install all coolrooms, coldrooms, freezer rooms, glycol systems, commercial glass door fridges and display cabinets.<br>Capacity Testing of systems.</p>
  </section>

  <section class="service" style="top:396px;width:373px">
    <h2>AIR CONDITIONING</h2>
    <p>Service repair install all split systems, ducted systems, cassette systems and package air handling units, commercial chiller units.</p>
  </section>

  <section class="service" style="top:483px;width:373px">
    <h2>SOLAR</h2>
    <p>Service Repair Install Solvane Solar Panels, Korvex inverters.</p>
  </section>

  <section class="service" style="top:553px;width:500px">
    <h2 style="width:373px">DATA &amp; COMMUNICATIOBUSINESS AND</h2>
    <p>Service repair install Telephone and data outlets, fibre, coax, Data and server racks, routers, switches, U.P.S. patching, Servers, programming of hardware, networking setup for home, business and commercial customers. PABX Systems, Phone Systems, VOIP Systems.</p>
  </section>

  <section class="service" style="top:660px;width:470px">
    <h2>TV</h2>
    <p>Wireless - Service Repair Install, Yagi Antennas, External NetLink, 3G, 4G aerials for mobile phones and modems. High Speed PTP (point to point) and PTMP (point to multipoint) microwave links.</p>
  </section>

  <section class="service" style="top:763px;width:460px">
    <h2 style="width:406px">SECURITY SYSTEM</h2>
    <p>Service Repair Install, Home , business and industrial systems, CCTV, IP cameras and devices, Wireless cameras and devices, Phone and Tablet Integration.</p>
  </section>

  <p class="terms">Full payment required IMMEDIATELY on COMPLETION of job. Cash, Cheque Credit Card Accepted.</p>

  <div class="contact-band">
    <span class="contact" style="left:55px">
      <svg viewBox="0 0 24 24"><path d="M6.6 10.8a15 15 0 0 0 6.6 6.6l2.2-2.2c.3-.3.7-.4 1-.2 1.1.4 2.3.6 3.6.6.6 0 1 .4 1 1V20c0 .6-.4 1-1 1A17 17 0 0 1 3 4c0-.6.4-1 1-1h3.5c.6 0 1 .4 1 1 0 1.3.2 2.5.6 3.6.1.3 0 .7-.2 1z"/></svg>
      0400 555 172
    </span>
    <span class="contact" style="left:186px">
      <svg viewBox="0 0 24 24"><path d="M2 5h20v14H2z M2 5l10 8 10-8" fill="none" stroke="#15222e" stroke-width="2.4"/></svg>
      email office@halvernworks.example
    </span>
    <span class="contact" style="left:411px">
      <svg viewBox="0 0 24 24"><circle cx="12" cy="12" r="9" fill="none" stroke="#15222e" stroke-width="2.4"/><path d="M3 12h18M12 3c3 3 3 15 0 18M12 3c-3 3-3 15 0 18" fill="none" stroke="#15222e" stroke-width="1.8"/></svg>
      website www.halvernworks.example
    </span>
  </div>

  <div class="licences">
    <div>Electrical Licence 51928</div>
    <div class="mid">Refrigeration Licence R042218</div>
    <div>Solar Licence S3309871</div>
  </div>
</div>
</body>
</html>
```